Fenwick and Torrance Postcard Design

Greetings!
Lawyers hire me as an expert witness. They take a gamble on hiring me in hopes of winning their case.
This postcard will be printed in jumbo size through Quillmark. The design must meet these specifications:

Full Bleed Size (starting document size)
11.12" x 6.12"
282 x 155 mm
3335 x 1835 pixels
* Finished artwork should use the full bleed dimensions for best results.
Document Trim Size (final size after being cut)
11.00" x 6.00"
279 x 152 mm
3300 x 1800 pixels
* Please be sure to keep all text and photos within the safe cutting margin.
Resolution
300 DPI
Visit Quillmark for more details or to download a design template:
https://www.quillmark-example.com/product-presentation-info.aspx?productPresentationId=1590#
https://www.quillmark-example.com/vp/ns/propath/UploadResources.aspx?selectedTab=0?pfid=BDW&pf_id=BDW&xnav=product-page#FileFormats

1. The postcard will have a Blank Backside.
2. I like a black, white and red color theme with a serious legalistic font.
3. In regards to color theme, see https://www.cardorbit-example.com/designs/security-system-postcards/#security-system-postcards-4
4. 8 preferred background images in alphabetical order from favorite to least favorite, but all are great:
a. https://files.driftbox-example.com/f/s!QwErTy12ZxCvBn34MnBvCx56LkJhGf
5. Header Text:
a. (line 1) Dr. K.R. Torrance, Psy.D., NCEB
b. (lines 2 and 3) Psychological Evaluator, Board-Certified Forensic Psychologist and National Expert Witness
c. (Line 4 in bold and more prominent than text in lines 1-3) 4 Signs of a Proficient & Credible Psyc. Expert
6. View this checklist image for inspiration, https://lnk.tidepoint-example.com/images/8RqWm3 and use the following text within such a checklist image:
7. Board Certified by the Continental Council of Courtroom Behavioral Science (CCCB)?
Yes, I'm Board Certified. This mark of proficiency in forensic psychology is recognized by judicial decisions, statutes and regulations.
8. Fellow of the Cont. Fellowship of Legal Behavioral Study?
Yes, I'm a CFLB Fellow, along with some of the field's most prominent leaders comprising the academic arm of the CCCB.
9. A Recognized Leader Amongst Other Experts?
I’m the 2018 duly elected President of the Hudson Valley Behavioral Guild Section on Courtroom Assessment, and a Board Member of the Coalition of Practitioners for Youth Safeguarding.
10. Positioned in Roles of Trust and Neutrality by Judges?
Yes, I work as an in-house Harborview Juvenile Tribunal mental-health expert in proceedings regarding competency, imminent risk, sentencing, custody, child maltreatment and TPR.
11. The following should be prominent along the bottom:
12. BOOK A LUNCH & LEARN AT YOUR OFFICE
Visit http://offer.witnessbench-example.com Call 555-014-2937
Designer: This call to action (CTA) for #12 needs to pop off of the page. It needs to draw the reader's eye. It needs depth, like the way a CTA button looks like on a website. Play around w/ idea to accomplish this (e.g., adding badges, icons, shapes, a picture, an image of someone presenting it, etc).
13. List my areas of specialization somewhere
• CPS & Matrimonial Issues
• Competency
• Juvenile Delinquency
• Criminal Sentencing
• Personal Injury and Civil Rights
• Immigration
• Fitness for Duty, SSD and Workers Comp
• Sex-Offenders
• IME and Neuropsychological Testing
• Behind-The-Scenes Consulting on A Contingency Fee
• Low-Price Initial Screening Evaluations
• Therapy Services & Programs for Litigants
14. Put this test somewhere and keep it subtle: I recognize the importance of your work. You can trust my assistance.
15. Put this in fine print somewhere (can be 2 lines): Fenwick and Torrance, LLC. 2018 New York Licensed Psychologist Lic. # 047213 - New Jersey Licensed Psychologist Lic. # 72K900315847

Target Market(s)

Lawyers

Industry/Entity Type

Hire

Font styles to use
Serif

Colors
ec1f27
ffffff

Requirements
Must have
• An awesome call to action. If the CTA doesn't catch the eye, then it won't work. The point of this postcard is to get them to that website so I can capture their email address. Anything else is a secondary gain. Consider 3-d design elements to give it pop and depth.
Should not have
• There's a big difference between a red rectangle and a red button on a website that has that 3d quality. This postcard has a lot of words. It can easily become just a bunch of text on a colorful piece of paper w/ a pic. Avoid this by segmenting the space, layering Diff color text on Diff color background and incorporating 3d design elements and shapes.

```html
<!DOCTYPE html>
<html lang="en">
<head>
<meta charset="utf-8">
<title>Fenwick and Torrance Postcard</title>
<link rel="stylesheet" href="https://fonts.googleapis.com/css2?family=Montserrat:wght@400;500;600;700&family=Oswald:wght@700&display=swap">
<style>
  :root {
    --red: #ec1f27;
    --red-deep: #b5121a;
    --white: #ffffff;
    --ink: #111111;
    --backdrop: #a4a4a4;
    --card-dark: #141414;
    --line-grey: #b8b8b8;
  }
  * { box-sizing: border-box; margin: 0; padding: 0; }
  html, body {
    width: 1200px; height: 1200px; overflow: hidden;
    background: var(--backdrop);
    font-family: "Montserrat", sans-serif;
  }
  .postcard {
    position: absolute; left: 163px; width: 875px; height: 481px;
    overflow: hidden;
  }
  .postcard--front { top: 107px; background: var(--card-dark); color: var(--white); }
  .postcard--back { top: 630px; background: var(--white); }

  .front-photo {
    position: absolute; inset: 0;
    background:
      radial-gradient(ellipse 40% 45% at 25% 30%, #3a2a22 0%, rgba(40,30,25,0) 70%),
      radial-gradient(ellipse 60% 60% at 60% 55%, #2a2a2a 0%, rgba(20,20,20,0) 70%),
      linear-gradient(135deg, #201b18 0%, #0c0c0c 100%);
  }

  .name-banner {
    position: absolute; left: 169px; top: 19px; width: 538px; height: 44px;
    background: linear-gradient(180deg, #ff3b40 0%, var(--red) 45%, var(--red-deep) 100%);
    border: 2px solid #ff8a8e; border-radius: 10px;
    box-shadow: 0 3px 6px rgba(0,0,0,.6);
    font-family: "Oswald", sans-serif; font-weight: 700; font-size: 34px;
    line-height: 40px; text-align: center; color: var(--white);
    text-shadow: 0 2px 2px rgba(0,0,0,.45);
  }
  .subtitle {
    position: absolute; left: 0; right: 0; top: 71px;
    text-align: center; font-weight: 500; font-size: 16px; line-height: 21px;
    padding-right: 0; width: 874px;
  }
  .headline {
    position: absolute; left: 120px; width: 634px; top: 113px;
    font-family: "Oswald", sans-serif; font-weight: 700; font-size: 27px;
    text-align: center; color: var(--red); line-height: 34px;
    text-shadow: 0 2px 3px rgba(0,0,0,.6);
  }
  .headline-rule {
    position: absolute; left: 179px; width: 520px; top: 150px; height: 2px;
    background: var(--white);
  }

  .checklist {
    position: absolute; left: 26px; top: 165px; width: 389px; height: 300px;
    background: linear-gradient(180deg, #e0232a 0%, var(--red-deep) 100%);
    border-radius: 24px;
    box-shadow: 0 4px 10px rgba(0,0,0,.6);
    padding: 16px 10px 0 0; overflow: hidden;
    list-style: none;
  }
  .checklist::before {
    content: ""; position: absolute; left: 6px; top: 6px; width: 380px; height: 150px;
    border-radius: 20px 20px 20px 80px;
    background: linear-gradient(180deg, rgba(255,255,255,.18), rgba(255,255,255,.05));
  }
  .checklist-item { position: relative; padding-left: 46px; margin-bottom: 7px; }
  .checklist-icon { position: absolute; left: 20px; top: 0; width: 15px; height: 15px; }
  .checklist-question { font-weight: 600; font-size: 10.5px; line-height: 12.5px; color: var(--ink); }
  .checklist-answer { font-weight: 400; font-size: 10.5px; line-height: 12.5px; margin-top: 3px; }

  .cta-title {
    position: absolute; left: 437px; top: 170px;
    font-weight: 700; font-size: 34px; line-height: 36px; letter-spacing: 1px;
    text-shadow: 0 3px 4px rgba(0,0,0,.7);
  }
  .cta-button {
    position: absolute; left: 437px; top: 210px; width: 243px; height: 32px;
    border: 2px solid var(--red); border-radius: 8px; padding: 3px;
    box-shadow: 0 3px 6px rgba(0,0,0,.7);
  }
  .cta-button span {
    display: block; height: 100%; background: linear-gradient(180deg, #ffffff, #e4e4e4);
    border-radius: 5px; color: var(--ink); font-weight: 500; font-size: 16px;
    line-height: 22px; padding-left: 7px; letter-spacing: .5px;
  }
  .contact-row {
    position: absolute; left: 437px; top: 251px;
    display: flex; align-items: center; gap: 6px;
    font-weight: 700; font-size: 11px;
  }
  .contact-row svg { width: 10px; height: 10px; }
  .contact-row .gap { width: 4px; }

  .specialties {
    position: absolute; left: 433px; top: 283px; width: 429px; height: 123px;
    border: 1.5px solid var(--white); border-radius: 16px;
  }
  .specialties-title {
    position: absolute; left: 6px; top: -10px; padding: 0 8px;
    background: #161616; font-weight: 600; font-size: 13.5px; line-height: 18px;
  }
  .specialties-list {
    position: absolute; list-style: none; font-size: 9.6px; line-height: 15.3px;
  }
  .specialties-list--left { left: 19px; top: 10px; width: 180px; }
  .specialties-list--right { left: 209px; top: 14px; width: 215px; }
  .specialties-list li { position: relative; padding-left: 0; }
  .specialties-list li::before {
    content: ""; position: absolute; left: -10px; top: 6px;
    width: 3.5px; height: 3.5px; border-radius: 50%; background: var(--red);
  }
  .specialties-list--right li.wrap { line-height: 12px; padding-bottom: 3px; padding-top: 2px; }

  .trust-line {
    position: absolute; left: 439px; top: 415px;
    color: var(--red); font-weight: 500; font-size: 10.5px;
  }
  .fine-print {
    position: absolute; left: 439px; top: 428px; width: 360px;
    font-size: 10.5px; line-height: 13.5px;
  }

  .back-photo {
    position: absolute; left: 0; top: 0; width: 560px; height: 481px;
    background: linear-gradient(120deg, #ececec 0%, #f4f4f4 45%, rgba(255,255,255,0) 100%);
  }
  .stamp-box {
    position: absolute; left: 766px; top: 31px; width: 70px; height: 70px;
    border: 2px solid var(--line-grey);
  }
  .address-line {
    position: absolute; left: 613px; width: 223px; height: 1.5px; background: var(--line-grey);
  }
</style>
</head>
<body>

<section class="postcard postcard--front">
  <div class="front-photo" role="img" aria-label="Dark photo of a judge's gavel on a wooden desk"></div>

  <h1 class="name-banner">DR. K.R. TORRANCE, PSY.D., NCEB</h1>
  <p class="subtitle">Psychological Evaluator, Board-Certified Forensic Psychologist<br>and National Expert Witness</p>
  <h2 class="headline">4 SIGNS OF A PROFICIENT &amp; CREDIBLE PSYC. EXPERT</h2>
  <div class="headline-rule"></div>

  <ul class="checklist">
    <li class="checklist-item">
      <svg class="checklist-icon" viewBox="0 0 16 16"><rect x="1" y="3" width="11" height="11" fill="none" stroke="#fff" stroke-width="1.8"/><path d="M3.5 8l3 3 8-9" fill="none" stroke="#fff" stroke-width="2"/></svg>
      <p class="checklist-question">Board Certified by the Continental Council of Courtroom Behavioral Science (CCCB)?</p>
      <p class="checklist-answer">Yes, I'm Board Certified. This mark of proficiency in forensic psychology is recognized by judicial decisions, statutes and regulations.</p>
    </li>
    <li class="checklist-item">
      <svg class="checklist-icon" viewBox="0 0 16 16"><rect x="1" y="3" width="11" height="11" fill="none" stroke="#fff" stroke-width="1.8"/><path d="M3.5 8l3 3 8-9" fill="none" stroke="#fff" stroke-width="2"/></svg>
      <p class="checklist-question">Fellow of the Cont. Fellowship of Legal Behavioral Study?</p>
      <p class="checklist-answer">Yes, I'm a CFLB Fellow, along with some of the field's most prominent leaders comprising the academic arm of the CCCB.</p>
    </li>
    <li class="checklist-item">
      <svg class="checklist-icon" viewBox="0 0 16 16"><rect x="1" y="3" width="11" height="11" fill="none" stroke="#fff" stroke-width="1.8"/><path d="M3.5 8l3 3 8-9" fill="none" stroke="#fff" stroke-width="2"/></svg>
      <p class="checklist-question">A Recognized Leader Amongst Other Experts?</p>
      <p class="checklist-answer">I'm the 2018 duly elected President of the Hudson Valley Behavioral Guild Section on Courtroom Assessment, and a Board Member of the Coalition of Practitioners for Youth Safeguarding.</p>
    </li>
    <li class="checklist-item">
      <svg class="checklist-icon" viewBox="0 0 16 16"><rect x="1" y="3" width="11" height="11" fill="none" stroke="#fff" stroke-width="1.8"/><path d="M3.5 8l3 3 8-9" fill="none" stroke="#fff" stroke-width="2"/></svg>
      <p class="checklist-question">Positioned in Roles of Trust and Neutrality by Judges?</p>
      <p class="checklist-answer">Yes, I work as an in-house Harborview Juvenile Tribunal mental-health expert in proceedings regarding competency, imminent risk, sentencing, custody, child maltreatment and TPR.</p>
    </li>
  </ul>

  <h2 class="cta-title">BOOK A LUNCH</h2>
  <div class="cta-button"><span>&amp; LEARN AT YOUR OFFICE</span></div>
  <p class="contact-row">
    <svg viewBox="0 0 10 10"><path d="M2 1l2 2-1 1.5c.6 1.2 1.3 1.9 2.5 2.5L7 6l2 2-1.3 1.3C4.5 9 1 5.5.7 2.3z" fill="#ec1f27"/></svg>
    <span>555-014-2937</span><span class="gap"></span>
    <svg viewBox="0 0 10 10"><circle cx="5" cy="5" r="4" fill="none" stroke="#ec1f27" stroke-width="1.5"/><path d="M1 5h8M5 1c-2 2.5-2 5.5 0 8M5 1c2 2.5 2 5.5 0 8" fill="none" stroke="#ec1f27" stroke-width="0.8"/></svg>
    <span>http://offer.witnessbench-example.com</span>
  </p>

  <div class="specialties">
    <h3 class="specialties-title">List my areas of specialization somewhere</h3>
    <ul class="specialties-list specialties-list--left">
      <li>CPS &amp; Matrimonial Issues</li>
      <li>Competency</li>
      <li>Juvenile Delinquency</li>
      <li>Criminal Sentencing</li>
      <li>Personal Injury and Civil Rights</li>
      <li>Immigration</li>
      <li>Sex-Offenders</li>
    </ul>
    <ul class="specialties-list specialties-list--right">
      <li>Fitness for Duty, SSD and Workers Comp</li>
      <li>IME and Neuropsychological Testing</li>
      <li class="wrap">Behind-The-Scenes Consulting on A Contingency Fee</li>
      <li>Low-Price Initial Screening Evaluations</li>
      <li>Therapy Services &amp; Programs for Litigants</li>
    </ul>
  </div>

  <p class="trust-line">I recognize the importance of your work. You can trust my assistance.</p>
  <p class="fine-print">Fenwick and Torrance, LLC. 2018 New York Licensed Psychologist Lic. # 047213 - New Jersey Licensed Psychologist Lic. # 72K900315847</p>
</section>

<section class="postcard postcard--back">
  <div class="back-photo" role="img" aria-label="Faint photo of classical courthouse columns"></div>
  <div class="stamp-box"></div>
  <div class="address-line" style="top:172px"></div>
  <div class="address-line" style="top:202px"></div>
  <div class="address-line" style="top:232px"></div>
  <div class="address-line" style="top:262px"></div>
</section>

</body>
</html>
```